NOTE: PAYMENT IS GUARANTEED for this project :)

++++++++++++++++++

I meant to share with you my mission for Caring Horizon:

To inspire nurses to take action that impacts change in their lives, their organizations, or even the world.

Values:
I – Integrity
M – Mentoring / Motivation
P – Passion for excellence
A – Accountability
C – Competence / knowledge/ achievement
T – Transformation – positive change

++++++++++++++++++

This is a Membership site so will need to show 'Members Login' etc.

Please make sure you use SUPER HIGH QUALITY PHOTOGRAPHY / IMAGES :)

This is a WORDPRESS site for my client - here's some questions I asked her with her answers:

1. Why do you want a website (or have your current site redesigned)?

I want a website to generate income, and residual income, promote quality education material to professionals that is not the same on-line programs point and click to answer questions. I want an interactive way to make a impact in nursing hence CaringHORIZON.

2. What’s your business/organization all about?

My parent company is Harbor Quill Advisory, LLC. I started it in 2001 and I provide consultative services to the legal and medical professionals. Mostly legal professionals; attorneys, and offer expert witness testimony. I also present full-day seminars regarding legal aspects of healthcare for nurses and hospital executive leaders. I am always promoting the professionalism in nursing where ever I can.

3. What sets your business apart from your competition?

What I will offer is instant access to quality and reliable clinical information and reliable business support for legal nurse consultants. I have not found another website that offers videos of clinical skills that nurses can watch over and over again without paying a lot of money for. Most of the information for nurses is through online learning read a packet, answer questions, and hopefully, maybe, they learned something. One of the reasons why my seminars are so well attended is they are interactive, and I use real examples to act out scenarios. I want nurses to be able to access short 7-10 minute video/podcasts that will show them how things are done and not just reading about it. Assessment skills will be performed on my family members in a clinic setting to create a realistic view. I want these to be somehow interactive if possible to reinforce the learning. Maybe you have some ideas on that.

For the legal nurse consultants. The programs are driving the “certification” outcome. When the nurses complete these programs, they have no experience and therefore are not able to recover their investment. I want to provide for them the same type of visual education support as the clinical nurses. These two audiences do not have to be mutually exclusive because they do tend to overlap in the real world.

I provide personal mentoring for novice legal nurse consultants in one week programs to support the application need in the LNC community. These weeks are valuable to the novice LNC trying to get started.

4. What problems does your business solve?

Application of concepts which is where I came up with Harbor Quill Advisory. I also have a tag with CaringHORIZON I have used: Education, training, application. I put the theory into practice. I translate the pages to the living people.

5. Who are your prospective customers or visitors?

Customers:
Nurses, Advanced Practice Nurses, Legal Nurse Consultants, Attorneys for the clinical/medical information, Universities that offer nursing programs,
Nursing students (I really want to pursue this niche, perhaps a discount for enrolled students???)

Visitors:
Hospital Chief Nursing Officers, Attorneys, Long Term Care Administrators, Faculty of Nursing programs.

6. What do you NOT want on your website?

A flat appearing, boxy, traditional site. I want the nurses to be able to navigate through without much effort, remember many are technologically challenged….
NOooo cartoons… not too many stock photos, I would rather take real images if at all possible to keep the site “alive and real”.

What do you like?

VRX.tv: the listing of videos is going to be important in my site because I will be making clinical example videos and interview videos that can be viewed over and over again by the Platinum members. I plan to have a blog and many downloads available as well.

Branvolt.com: I like the layout but I do want more interaction with mine. I do like the are you a training leader? Department leader: emerging leader? Componenets because I am addressing Nurses, Nurse Leaders, Legal Nurse Consultants… this would be important to establish right up front. I particularly like the video enhanced special report the new prospect has access to. I will do this for my site. I think it is also cool that you can change the color of the landing page to your liking.

www.thelomrickteam.example: I like a lot of things on this website but it is a bit difficult to navigate for even me. I like the short one minute capture of audio cds. I do plan to have CD material available. I do like the what you get with each level of membership under lomricklink tab. Some of the pages are not easy to read because the color is too dark and the font color is not contrasted enough. I like the tips in ten downloads on CD as well. I can see this working with mine as similar formatting with of course difference content.

www.dorindavesk.example: I do like the section she has on photo gallery where I can post event that have taken place as I speak, and work one-on-one with nurses across the country. (not the fashion shoot ?).

www.9forward.example: I love the rollover interaction, the eyes constantly moving to the movement across the site.
http://www.belworth.example/BelworthMedia.aspx?VideoId=4830127795004&type=M Quick lane video using sketchpad is a cool idea.

www.plumvault.example - nice and clean

11. Please give us a list of websites that you DON’T Like and Why you Don’t like them.

www.torq.example: landing page is way too crowded, too many colors, I don’t know where to go for what I would be looking for. Font is too small with large amounts of content.

www.quillcare.example: this site is way too busy and difficult to navigate however I do like the page titled: Memorable RVTA cases. I would use a page like this for memorable Caring Horizon experiences that would encourage others and remember the great things nurses do.

www.wardlearn.example: Do not like at all. Way to juvenile.

Colour Scheme:

The colors palette I like is…. I think you will get the general idea of the color scheme. I like the yellow on dark colors so it pops, make sense?

F7C40E
4819A9
2E1FAC
F7D80E

Payment is guaranteed for this project now! :)

Thank you

Target Market(s)

Customers: Nurses, Advanced Practice Nurses, Legal Nurse Consultants, Attorneys for the clinical/medical information, Universities that offer nursing

Values:
I – Integrity
A – Accountability

Industry/Entity Type

Healthcare

Requirements
Must have
• professional, clean, VERY HIGH QUALITY IMAGES/ PHOTOGRAPHY e.g. PixBarrel
Nice to have
• Dorian:
I have shown the design template to several people to get their first impression. I was shocked. They thought of the Wexbury Falcons! The football team. Ouch. I don’t want that. Crazy what others see.
Can we please change the color scheme to incorporate the colors below with the same layout. The Layout is good, it is the color I need to work a bit more on. Sorry about this but I don’t want to be a Falcons fan.

336699
FFCC66
FFFFFF
003366

Miriam

New logo required: Caring Horizon - DO NOT USE MEDICAL
Should not have
• childish graphics, or icons.
Don't want to see unprofessional site with clumsy type or template type designs. We can include some photos.

```html
<!DOCTYPE html>
<html lang="en">
<head>
<meta charset="utf-8">
<title>Caring Horizon</title>
<link rel="stylesheet" href="https://fonts.googleapis.com/css2?family=Roboto+Condensed:wght@400;700&family=PT+Sans:wght@400;700&family=Arimo:wght@400;700&display=swap">
<style>
:root{
  --blue:#1677c4;
  --blue-dark:#0d66a8;
  --blue-light:#2a8fd6;
  --gold:#ffcc66;
  --page:#f2f2f2;
  --ink:#4a4a4a;
  --ink-soft:#6a6a6a;
  --line:#d9d9d9;
  --white:#ffffff;
}
*{box-sizing:border-box;margin:0;padding:0}
html,body{width:1200px;height:3197px;overflow:hidden}
body{position:relative;background:var(--page);font-family:"PT Sans",Tahoma,sans-serif;color:var(--ink)}
.abs{position:absolute}
.site-header{left:0;top:0;width:1200px;height:96px;background:var(--white);border-bottom:3px solid var(--blue)}
.brand{left:124px;top:14px;font-family:"Roboto Condensed",sans-serif;font-weight:700;font-size:36px;letter-spacing:2px;color:#6fa7d2}
.hero{left:100px;top:99px;width:1000px;height:289px;background:linear-gradient(100deg,#7fd3db 0%,#cfe9ee 30%,#f2f6f8 50%,#9bdbe0 72%,#4f8fc0 100%)}
.nav{left:100px;top:388px;width:1000px;height:42px;background:var(--blue);display:flex;align-items:center;font-family:"Arimo",sans-serif;font-weight:700;font-size:16px;color:var(--white)}
.nav .home{width:56px;height:42px;display:flex;align-items:center;justify-content:center;border-right:1px solid #3d8fd0}
.nav .item{height:42px;display:flex;align-items:center;padding:0 24px;border-right:1px solid #3d8fd0}
.nav .item.active span{background:#0b5a96;color:var(--gold);padding:4px 8px}
.nav .search{margin-left:auto;margin-right:26px;width:218px;height:28px;background:var(--white);color:#7aa9cf;font-weight:400;font-size:14px;padding:5px 12px}
.welcome{left:0;top:510px;width:1200px;text-align:center;font-family:"Roboto Condensed",sans-serif;font-weight:700;font-size:62px;color:var(--blue-dark);letter-spacing:1px}
.intro{left:124px;top:620px;width:964px;font-size:22.5px;line-height:26px;color:#555}
.col-divider{top:805px;width:2px;height:500px;background:var(--blue-light)}
.role{top:805px;width:320px}
.role h2{font-family:"Roboto Condensed",sans-serif;font-weight:700;font-size:27px;color:var(--blue);text-align:center}
.role .photo{margin:24px auto 0;width:241px;height:162px;background:linear-gradient(160deg,#4a3b33,#8a7c6c 55%,#2e2a28)}
.role p{margin-top:58px;font-size:15.5px;line-height:19.5px;color:#555}
.section-title{left:128px;top:1362px;font-family:"PT Sans",sans-serif;font-size:32px;color:var(--blue-light)}
.video-main{left:124px;top:1423px;width:611px;height:269px;background:linear-gradient(110deg,#dfe6ea,#b9c9d3 45%,#e9ddd6 70%,#c7b3a6)}
.video-main .play{left:278px;top:72px;width:72px;height:72px;background:var(--blue)}
.video-main .caption{left:0;bottom:0;width:611px;height:72px;background:rgba(40,45,55,.72);color:var(--white);font-family:"Arimo",sans-serif;font-weight:700;font-size:12.5px;line-height:16px;padding:16px 14px}
.thumb{left:765px;width:311px;height:81px;background:var(--blue)}
.thumb .pic{left:8px;top:8px;width:132px;height:65px;background:linear-gradient(120deg,#f4efe8,#e6c79f 50%,#f1e7da)}
.thumb .txt{left:150px;top:10px;width:150px;font-family:"Arimo",sans-serif;font-weight:700;font-size:11px;line-height:14px;color:var(--white)}
.thumb .view{left:234px;top:54px;width:60px;height:19px;background:var(--white);color:var(--blue);font-family:"Arimo",sans-serif;font-weight:700;font-size:11px;text-align:center;line-height:19px}
.widget{left:124px;width:304px;background:var(--white);box-shadow:0 6px 6px -4px rgba(0,0,0,.35)}
.widget-head{height:26px;background:var(--blue);color:var(--white);font-size:17px;line-height:26px;padding-left:44px;position:relative}
.widget-head .mark{position:absolute;left:12px;top:3px;width:20px;height:20px;border-radius:50%;background:#6fb6ea}
.tweet{margin:0 10px;padding:10px 0 8px;border-bottom:1px solid var(--line);font-size:12.5px;line-height:16px;color:#444}
.tweet a{color:var(--blue)}
.tweet small{display:block;margin-top:4px;font-size:10px;color:var(--blue);text-decoration:underline}
.fb-body{margin:10px;border:1px solid #cfcfcf;padding:8px;height:323px}
.fb-top{display:flex;gap:8px}
.fb-top .sq{width:42px;height:42px;background:#b8c3cf}
.fb-top b{color:#3b5998;font-size:14px}
.fb-top .like{font-size:11px;color:#555;margin-top:4px}
.fb-count{font-size:11px;margin:12px 0 6px}
.faces{display:grid;grid-template-columns:repeat(5,48px);gap:6px 6px}
.face{font-size:9px;text-align:center;color:#555}
.face i{display:block;width:44px;height:44px;margin:0 auto 3px;background:linear-gradient(160deg,#9aa3ab,#5d646b)}
.fb-foot{font-size:9px;color:#3b5998;margin-top:10px}
.post{left:469px;width:622px;background:var(--white);border:1px solid #dcdcdc;box-shadow:0 8px 6px -5px rgba(0,0,0,.35)}
.post .pic{left:21px;top:21px;width:580px;height:175px;background:linear-gradient(100deg,#c8ecf0,#7fd0d8 35%,#eef5f7 60%,#8fd6dd 85%,#5aa0c8)}
.post .meta{left:21px;top:210px;font-size:11px;color:#555}
.post .meta a{color:var(--blue)}
.post h3{position:absolute;left:21px;top:236px;font-weight:400;font-size:19px;color:#222}
.post p{position:absolute;left:21px;top:272px;width:580px;font-size:12px;line-height:15.5px;color:#555}
.post .more{right:21px;font-size:12px;color:var(--blue);text-decoration:underline}
.post .ribbon{right:-2px;top:206px;width:86px;height:36px}
.footer{left:0;top:3126px;width:1200px;height:71px;background:#f8f8f8}
.footer .copy{left:139px;top:18px;font-size:12px;color:var(--blue)}
.to-top{left:1010px;top:3094px;width:64px;height:64px;border-radius:50%;background:var(--blue);border:3px solid var(--white);box-shadow:0 0 0 2px var(--blue);color:var(--white);font-size:17px;text-align:center;line-height:58px}
</style>
</head>
<body>

<header class="site-header abs"></header>
<div class="brand abs">CARING HORIZON</div>
<div class="hero abs" role="img" aria-label="Two surgeons in caps and masks looking down into the camera"></div>

<nav class="nav abs">
  <div class="home"><svg width="20" height="18" viewBox="0 0 20 18"><path d="M10 1 1 9h3v8h4v-5h4v5h4V9h3z" fill="#fff"/></svg></div>
  <div class="item">Home</div>
  <div class="item active"><span>Treaning</span></div>
  <div class="item">Vedios</div>
  <div class="item">Depoimentos</div>
  <div class="item">Blog</div>
  <div class="item">Contact</div>
  <div class="search">Search . .</div>
</nav>

<h1 class="welcome abs">WELCOME TO CARING HORIZON</h1>
<p class="intro abs">Branvolt is the development hub for emerging leaders. The development of Emerging Leaders throughout the entire organization is critical for success. Branvolt is an easy to deploy web-based, video-based supplement to existing leadership curriculum. Content is executive tested and brought to you by some of the best leadership minds available.</p>

<div class="col-divider abs" style="left:432px"></div>
<div class="col-divider abs" style="left:782px"></div>

<section class="role abs" style="left:96px">
  <h2>Are you a training leader?</h2>
  <div class="photo" role="img" aria-label="Empty seminar room with projector screens"></div>
  <p style="padding:0 0 0 28px;width:300px">It’s difficult to educate the elusive emerging leader. It’s costly and logistically complex to get them all in a centrally convenient classroom. And if you do, follow-up is a challenge. Branvolt can be just the supplement you need to meet your mission. Click to learn more about how to get started with the built in testing process.</p>
</section>
<section class="role abs" style="left:451px">
  <h2>Are you a department leader?</h2>
  <div class="photo" role="img" aria-label="Speaker presenting to a seated audience"></div>
  <p style="padding:0 20px">You recognize that the education of your emerging leaders is your responsibility, with the help of your education department. Is attending a one-off class for some of your team doing the trick? Use Branvolt to start the conversations you must have to pass along leadership wisdom and grow your organization. With no infrastructure, you can take the reins.</p>
</section>
<section class="role abs" style="left:797px">
  <h2>Are you an emerging leader?</h2>
  <div class="photo" role="img" aria-label="Group of people at a workshop"></div>
  <p style="padding:0 20px">Are you used to learning what you need to know when you need to know it? Whether you work on your own or in a traditional corporate environment, do you wait for the standard learning opportunities that come along or take the initiative? Give yourself a leg up with Branvolt. Learn more by trying Branvolt with a no-obligation full access 14 day trial.</p>
</section>

<h2 class="section-title abs">TRANING VEDIOS</h2>
<div class="video-main abs">
  <div class="abs" style="inset:0" role="img" aria-label="Doctor performing an ultrasound on a smiling patient"></div>
  <div class="play abs"><svg width="72" height="72" viewBox="0 0 72 72"><path d="M29 22v28l22-14z" fill="#fff"/></svg></div>
  <div class="caption abs">Now I have lots of attorneys asking for my "GBU" reports. They're three to five pages long and take five to ten hours to complete. I do five or ten GBUs a week, and they're really fun.</div>
</div>
<div class="thumb abs" style="top:1423px"><div class="pic abs" role="img" aria-label="Smiling woman resting"></div><div class="txt abs">Now I have lots of attorneys for my "GBU" reports.</div><div class="view abs">View</div></div>
<div class="thumb abs" style="top:1517px"><div class="pic abs" role="img" aria-label="Smiling woman resting"></div><div class="txt abs">Now I have lots of attorneys for my "GBU" reports.</div><div class="view abs">View</div></div>
<div class="thumb abs" style="top:1611px"><div class="pic abs" role="img" aria-label="Smiling woman resting"></div><div class="txt abs">Now I have lots of attorneys for my "GBU" reports.</div><div class="view abs">View</div></div>

<aside class="widget abs" style="top:1786px;height:383px">
  <div class="widget-head"><span class="mark"></span>Tweets</div>
  <div class="tweet">You recognize that the education of your emerging leaders<a>http://shrtl.example/plkg6</a><small>about 6 hours ago</small></div>
  <div class="tweet">You recognize that the education of your emerging leaders <a>http://shrtl.example/plkg6</a><small>about 6 hours ago</small></div>
  <div class="tweet">You recognize that the education of your emerging leaders <a>http://shrtl.example/plkg6</a><small>about 6 hours ago</small></div>
  <div class="tweet">You recognize that the education of your emerging leaders <a>http://shrtl.example/plkg6</a><small>about 6 hours ago</small></div>
  <div class="tweet" style="border:0">70 Must-Have CSS3 and HTML5 Tutorials and Resources <a>http://shrtl.example/plkg6</a><small>about 6 hours ago</small></div>
</aside>

<aside class="widget abs" style="top:2244px;height:381px">
  <div class="widget-head" style="padding-left:40px"><span class="mark" style="border-radius:0;background:#fff;width:18px;height:18px;top:4px"></span>Friendbook</div>
  <div class="fb-body">
    <div class="fb-top"><div class="sq"></div><div><b>MarcelinoCoder</b> <span style="font-size:10px">on Friendbook</span><div class="like">Liked &nbsp; You like this.</div></div></div>
    <div class="fb-count">13 people like <b>MarcelinoCoder</b>.</div>
    <div class="faces">
      <div class="face"><i></i>Ravel</div><div class="face"><i></i>Odilia</div><div class="face"><i></i>Odilia</div><div class="face"><i></i>Tamires Lu</div><div class="face"><i></i>Jucara</div>
      <div class="face"><i></i>Ravel</div><div class="face"><i></i>Odilia</div><div class="face"><i></i>Odilia</div><div class="face"><i></i>Tamires Lu</div><div class="face"><i></i>Jucara</div>
      <div class="face"><i></i>Davino</div><div class="face"><i></i>Elton</div><div class="face"><i></i>Rania</div><div class="face"><i></i>Iury</div><div class="face"><i></i>Ravel</div>
    </div>
    <div class="fb-foot">■ Social plugin</div>
  </div>
</aside>

<article class="post abs" style="top:1786px;height:409px">
  <div class="pic abs" role="img" aria-label="Surgeon in cap and mask"></div>
  <div class="meta abs">12 de dezembro de 2011 por <a>Admin</a></div>
  <svg class="ribbon abs" viewBox="0 0 86 36"><path d="M0 0h86v36H0l10-18z" fill="#1677c4"/><path d="M22 9h24a5 5 0 0 1 5 5v6a5 5 0 0 1-5 5H32l-7 5 2-5h-5a5 5 0 0 1-5-5v-6a5 5 0 0 1 5-5z" fill="#333"/><text x="60" y="26" font-family="PT Sans,sans-serif" font-weight="700" font-size="21" fill="#fff">5</text></svg>
  <h3>Lorem ipsum dolor sit amet, consectetur adipiscing elit.</h3>
  <p>Lorem ipsum dolor sit amet, consectetur adipiscing elit. In massa libero, interdum quis ullamcorper a, pellentesque nec tellus. Donec sit amet lectus a nisi sagittis consequat sed vitae mauris. Quisque ut diam ligula, sed viverra tellus. Curabitur suscipit dignissim odio vel porttitor. Vestibulum dignissim justo eu nisl vestibulum ultricies. Nullam egestas dictum ipsum in eleifend. Morbi tellus nisl, ultrices vitae consectetur non, tincidunt in risus. Morbi tellus nisl, ultrices vitae consectetur non, tincidunt in risus...</p>
  <span class="more abs" style="top:382px">Leia mais...</span>
</article>

<article class="post abs" style="top:2227px;height:411px">
  <div class="pic abs" role="img" aria-label="Surgeon in cap and mask"></div>
  <div class="meta abs">12 de dezembro de 2011 por <a>Admin</a></div>
  <svg class="ribbon abs" viewBox="0 0 86 36"><path d="M0 0h86v36H0l10-18z" fill="#1677c4"/><path d="M22 9h24a5 5 0 0 1 5 5v6a5 5 0 0 1-5 5H32l-7 5 2-5h-5a5 5 0 0 1-5-5v-6a5 5 0 0 1 5-5z" fill="#333"/><text x="60" y="26" font-family="PT Sans,sans-serif" font-weight="700" font-size="21" fill="#fff">5</text></svg>
  <h3>Lorem ipsum dolor sit amet, consectetur adipiscing elit.</h3>
  <p>Lorem ipsum dolor sit amet, consectetur adipiscing elit. In massa libero, interdum quis ullamcorper a, pellentesque nec tellus. Donec sit amet lectus a nisi sagittis consequat sed vitae mauris. Quisque ut diam ligula, sed viverra tellus. Curabitur suscipit dignissim odio vel porttitor. Vestibulum dignissim justo eu nisl vestibulum ultricies. Nullam egestas dictum ipsum in eleifend. Morbi tellus nisl, ultrices vitae consectetur non, tincidunt in risus. Morbi tellus nisl, ultrices vitae consectetur non, tincidunt in risus...</p>
  <span class="more abs" style="top:384px">Leia mais...</span>
</article>

<article class="post abs" style="top:2668px;height:396px">
  <div class="pic abs" role="img" aria-label="Surgeon in cap and mask"></div>
  <div class="meta abs">12 de dezembro de 2011 por <a>Admin</a></div>
  <svg class="ribbon abs" viewBox="0 0 86 36"><path d="M0 0h86v36H0l10-18z" fill="#1677c4"/><path d="M22 9h24a5 5 0 0 1 5 5v6a5 5 0 0 1-5 5H32l-7 5 2-5h-5a5 5 0 0 1-5-5v-6a5 5 0 0 1 5-5z" fill="#333"/><text x="60" y="26" font-family="PT Sans,sans-serif" font-weight="700" font-size="21" fill="#fff">5</text></svg>
  <h3>Lorem ipsum dolor sit amet, consectetur adipiscing elit.</h3>
  <p>Lorem ipsum dolor sit amet, consectetur adipiscing elit. In massa libero, interdum quis ullamcorper a, pellentesque nec tellus. Donec sit amet lectus a nisi sagittis consequat sed vitae mauris. Quisque ut diam ligula, sed viverra tellus. Curabitur suscipit dignissim odio vel porttitor. Vestibulum dignissim justo eu nisl vestibulum ultricies. Nullam egestas dictum ipsum in eleifend. Morbi tellus nisl, ultrices vitae consectetur non, tincidunt in risus. Morbi tellus nisl, ultrices vitae consectetur non, tincidunt in risus...</p>
  <span class="more abs" style="top:370px">Leia mais...</span>
</article>

<footer class="footer abs"><div class="copy abs">Copyright © caring horizon 2012</div></footer>
<div class="to-top abs">top</div>

</body>
</html>
```